Stonebell Inc Ad Design, trying to attract new customers

Please see attached pictures and files for information
We are a Class A - Residential General Contractor in Lynchburg, VA with Master HVAC and Master PLUMBING Licenses. We focus on Water and Air Solutions for property owners.
We build, remodel, and repair homes
We do HVAC, including Humidity Control and Air Purification
We do Plumbing
We love to fix Water Leaks for Plumbing, Roof Leaks, Skylight Leaks, Basement Leaks, Foundation Leaks, Door and Window Leaks
We solve water and air issues on the outside of properties with custom structures, grading, and landscaping

Target Market(s)

Residential and Light Commercial property owners

Industry/Entity Type

Construction

Font styles to use
Other font styles liked:
• see cards

Colors
0054AA
0677BA
7BADD7
CADEEF
E8F1F8
00AB8E
00BBA5
67D7C9
C6EFE9
E9F9F6

Requirements
Must have
• See business cards
Nice to have
• see business cards
Should not have
• My name

```html
<!DOCTYPE html>
<html lang="en">
<head>
<meta charset="utf-8">
<title>Stonebell Inc – Billboard</title>
<link href="https://fonts.googleapis.com/css2?family=Poppins:wght@500;600;700;800&family=Rubik:wght@500;600&display=swap" rel="stylesheet">
<style>
  :root{
    --ink:#0b0b0b;
    --blue:#1a8fd4;
    --blue-deep:#0677ba;
    --green:#6ab23e;
    --white:#ffffff;
    --page:#e9edf1;
    --photo-light:#dfe4ea;
    --photo-mid:#8c97a6;
    --photo-dark:#3d4b63;
  }
  *{box-sizing:border-box;margin:0;padding:0}
  html,body{width:1200px;height:857px;overflow:hidden;background:var(--page)}
  .canvas{position:relative;width:1200px;height:857px}
  .board{position:absolute;left:20px;top:130px;width:1160px;height:596px;background:var(--white);overflow:hidden;box-shadow:0 4px 18px rgba(0,0,0,.15)}
  .photo-layer{position:absolute;inset:0}
  .brand-pill{position:absolute;right:0;top:10px;width:180px;height:62px;background:var(--white);border-radius:31px 0 0 31px;display:flex;align-items:center;justify-content:center;gap:8px}
  .brand-pill .dot{width:14px;height:14px;border-radius:50%;background:var(--green)}
  .brand-pill .name{font-family:'Poppins',sans-serif;font-weight:700;font-size:19px;color:var(--blue);letter-spacing:.5px}
  .headline{position:absolute;left:40px;top:52px;font-family:'Poppins',sans-serif;font-weight:800;line-height:59px;font-size:56px;letter-spacing:-1px}
  .headline .line{display:block;white-space:nowrap}
  .headline .black{color:var(--ink)}
  .headline .blue{color:var(--blue)}
  .headline .green{color:var(--green)}
  .headline .class-line{font-weight:700;font-size:54px}
  .lead{position:absolute;left:40px;top:306px;font-family:'Rubik',sans-serif;font-weight:500;font-size:17px;color:var(--ink)}
  .service-band{position:absolute;left:0;top:337px;width:530px;height:48px;background:var(--green);display:flex;align-items:center;padding-left:40px;font-family:'Poppins',sans-serif;font-weight:700;font-size:22px;color:var(--white)}
  .leak-list{position:absolute;left:0;top:385px;width:546px;height:136px;background:var(--blue);padding:12px 20px 0 36px;display:flex;flex-wrap:wrap;column-gap:20px;row-gap:14px;list-style:none;align-content:flex-start}
  .leak-list li{display:flex;align-items:center;gap:7px;font-family:'Poppins',sans-serif;font-weight:600;font-size:14.5px;color:var(--white);white-space:nowrap}
  .leak-list li.break-after{margin-right:200px}
  .tick{width:20px;height:20px;flex:none}
  .contact-row{position:absolute;left:36px;top:532px;display:flex;align-items:center;gap:16px;font-family:'Poppins',sans-serif;font-weight:500;font-size:18px;color:var(--ink)}
  .contact-row .item{display:flex;align-items:center;gap:7px}
  .contact-row .icon{width:26px;height:26px;border-radius:4px;background:var(--green);display:flex;align-items:center;justify-content:center}
</style>
</head>
<body>
<div class="canvas">
  <section class="board">
    <svg class="photo-layer" width="1160" height="596" viewBox="0 0 1160 596">
      <defs>
        <linearGradient id="photoTone" x1="0" y1="0" x2="1" y2="1">
          <stop offset="0" stop-color="var(--photo-light)"/>
          <stop offset=".55" stop-color="var(--photo-mid)"/>
          <stop offset="1" stop-color="var(--photo-dark)"/>
        </linearGradient>
      </defs>
      <path role="img" aria-label="Photo of a plumber in overalls and gloves repairing the pipes under a bathroom sink" d="M770 0 C612 150 572 450 652 596 L1160 596 L1160 0 Z" fill="url(#photoTone)"/>
      <path d="M742 0 C584 150 544 450 624 596" fill="none" stroke="var(--green)" stroke-width="5"/>
    </svg>

    <div class="brand-pill"><span class="dot"></span><span class="name">STONEBELL</span></div>

    <h1 class="headline">
      <span class="line"><span class="black">WE PUT </span><span class="blue">WATER AND</span></span>
      <span class="line green">AIR IN ITS PLACE</span>
      <span class="line black class-line">Class A RBC</span>
      <span class="line"><span class="blue">PLUMBING </span><span class="green">HVAC</span></span>
    </h1>

    <p class="lead">We do HVAC, including Humidity Control and Air Purification</p>

    <div class="service-band">We Build, Remodel, And Repair Homes</div>

    <ul class="leak-list">
      <li><svg class="tick" viewBox="0 0 20 20"><rect x="1" y="3" width="16" height="16" fill="none" stroke="#fff" stroke-width="1.6"/><path d="M4 10 L8 15 L18 1" fill="none" stroke="#fff" stroke-width="2"/></svg>We love to fix Water Leaks for Plumbing</li>
      <li><svg class="tick" viewBox="0 0 20 20"><rect x="1" y="3" width="16" height="16" fill="none" stroke="#fff" stroke-width="1.6"/><path d="M4 10 L8 15 L18 1" fill="none" stroke="#fff" stroke-width="2"/></svg>Roof Leaks</li>
      <li><svg class="tick" viewBox="0 0 20 20"><rect x="1" y="3" width="16" height="16" fill="none" stroke="#fff" stroke-width="1.6"/><path d="M4 10 L8 15 L18 1" fill="none" stroke="#fff" stroke-width="2"/></svg>Skylight Leaks</li>
      <li><svg class="tick" viewBox="0 0 20 20"><rect x="1" y="3" width="16" height="16" fill="none" stroke="#fff" stroke-width="1.6"/><path d="M4 10 L8 15 L18 1" fill="none" stroke="#fff" stroke-width="2"/></svg>Basement Leaks</li>
      <li><svg class="tick" viewBox="0 0 20 20"><rect x="1" y="3" width="16" height="16" fill="none" stroke="#fff" stroke-width="1.6"/><path d="M4 10 L8 15 L18 1" fill="none" stroke="#fff" stroke-width="2"/></svg>Foundation Leaks</li>
      <li><svg class="tick" viewBox="0 0 20 20"><rect x="1" y="3" width="16" height="16" fill="none" stroke="#fff" stroke-width="1.6"/><path d="M4 10 L8 15 L18 1" fill="none" stroke="#fff" stroke-width="2"/></svg>Door and Window Leaks</li>
    </ul>

    <div class="contact-row">
      <span class="item"><span class="icon"><svg width="16" height="16" viewBox="0 0 24 24"><path d="M6.6 10.8a15 15 0 0 0 6.6 6.6l2.2-2.2c.3-.3.7-.4 1-.2 1.1.4 2.3.6 3.6.6.6 0 1 .4 1 1V20c0 .6-.4 1-1 1A17 17 0 0 1 3 4c0-.6.4-1 1-1h3.5c.6 0 1 .4 1 1 0 1.3.2 2.5.6 3.6.1.3 0 .7-.2 1z" fill="#fff"/></svg></span>(434) 555-0172</span>
      <span class="item"><span class="icon"><svg width="16" height="16" viewBox="0 0 24 24"><circle cx="12" cy="12" r="9" fill="none" stroke="#fff" stroke-width="2"/><path d="M3 12h18M12 3c3 3 3 15 0 18M12 3c-3 3-3 15 0 18" fill="none" stroke="#fff" stroke-width="1.6"/></svg></span>CONTACT@STONEBELLVA.COM</span>
    </div>
  </section>
</div>
</body>
</html>
```